Veranta - Solution provider in business consulting

Veranta is a swiss based company providing solutions for developing markets. The business covers various fields of business consulting, such as supply chain, product costs, quality management and manufacturing management. The Business operates in a efficient, straight and solution oriented manner.
The final design should communicate these characteristics. Asian people as well as as western people shall identify the qualities of the company at first sight.
The customer needs business cards with a simple view but an recognizable design, printed in high quality. Engraved elements such as the globe or simple words are possible.
Available colors are: (RAL)
102/102/102
51/102/102
153/204/153
255/102/51
Font: Calibri
Industry/Entity Type
Business
Look and feel
Each slider illustrates characteristics of the customer's brand and the style your logo design should communicate.

```html
<!DOCTYPE html>
<html lang="en">
<head>
<meta charset="utf-8">
<title>Veranta — Business Card</title>
<link href="https://fonts.googleapis.com/css2?family=Carlito:wght@400;700&display=swap" rel="stylesheet">
<style>
  :root {
    --page-bg: #d9d6d1;
    --card-top: #6e6e6e;
    --card-bottom: #555555;
    --ink: #f2f2f2;
    --ink-soft: #d8d8d8;
    --rule: #e6e6e6;
  }
  * { margin: 0; padding: 0; box-sizing: border-box; }
  html, body {
    width: 1200px; height: 1022px; overflow: hidden;
    background: var(--page-bg);
    font-family: "Carlito", "Calibri", sans-serif;
  }
  .stage {
    width: 1200px; height: 1022px;
    display: flex; align-items: center; justify-content: center;
  }
  .card {
    position: relative;
    width: 840px; height: 480px;
    border-radius: 22px;
    background: linear-gradient(160deg, var(--card-top), var(--card-bottom));
    box-shadow: 0 18px 40px rgba(0,0,0,0.25);
    overflow: hidden;
    color: var(--ink);
  }
  .brand {
    position: absolute; left: 0; right: 0; top: 70px;
    display: flex; align-items: center; justify-content: center; gap: 22px;
  }
  .brand-dot {
    width: 74px; height: 74px; border-radius: 50%;
    background: var(--ink);
  }
  .brand-name {
    font-size: 104px; font-weight: 400; letter-spacing: 1px; line-height: 1;
    color: var(--ink);
  }
  .rule {
    position: absolute; left: 150px; right: 40px; top: 292px;
    height: 2px; background: var(--rule);
  }
  .tab {
    position: absolute; left: -26px; top: 250px;
    width: 66px; height: 46px;
    border: 3px solid var(--ink); border-radius: 12px;
  }
  .person { position: absolute; left: 60px; top: 252px; }
  .person-name { font-size: 32px; font-weight: 700; line-height: 1; }
  .person-role {
    margin-top: 10px; font-size: 18px; color: var(--ink-soft);
    display: flex; align-items: center; gap: 6px;
  }
  .person-role::after {
    content: ""; width: 80px; height: 2px; background: var(--rule);
  }
  .address {
    position: absolute; left: 60px; top: 370px;
    font-size: 20px; line-height: 1.35; color: var(--ink-soft);
  }
  .contacts {
    position: absolute; right: 40px; top: 312px;
    list-style: none; text-align: right;
    font-size: 20px; line-height: 1.35; color: var(--ink-soft);
  }
  .contacts li { display: flex; justify-content: flex-end; align-items: center; gap: 10px; }
  .contacts svg { width: 16px; height: 16px; fill: none; stroke: var(--ink); stroke-width: 1.6; }
</style>
</head>
<body>
<main class="stage">
  <article class="card">
    <div class="brand">
      <span class="brand-dot"></span>
      <span class="brand-name">Veranta</span>
    </div>

    <div class="tab"></div>
    <div class="rule"></div>

    <div class="person">
      <p class="person-name">Marco Keller</p>
      <p class="person-role">CEO</p>
    </div>

    <address class="address" style="font-style:normal">
      Veranta GmbH Lindenhof<br>
      14 8610 Uster Switzerland
    </address>

    <ul class="contacts">
      <li>+41 79 382 5507
        <svg viewBox="0 0 16 16"><rect x="4" y="1.5" width="8" height="13" rx="1.5"/><line x1="7" y1="12" x2="9" y2="12"/></svg>
      </li>
      <li>+41 71 264 8813
        <svg viewBox="0 0 16 16"><path d="M4 2l2.5 3-1.5 1.5c1 2 2.5 3.5 4.5 4.5L11 9.5l3 2.5-1.5 2C7 14 2 9 2 3.5z"/></svg>
      </li>
      <li>marco.keller@veranta.ch
        <svg viewBox="0 0 16 16"><rect x="1.5" y="3.5" width="13" height="9" rx="1"/><path d="M1.5 4l6.5 5 6.5-5"/></svg>
      </li>
      <li>www.veranta.ch
        <svg viewBox="0 0 16 16"><circle cx="8" cy="8" r="6.5"/><ellipse cx="8" cy="8" rx="2.8" ry="6.5"/><line x1="1.5" y1="8" x2="14.5" y2="8"/></svg>
      </li>
    </ul>
  </article>
</main>
</body>
</html>
```